a graphic model of stress response for online learning course

We need a model of how the brain experiences, interprets and responds to stressors. There are three components to this.

I need a simple linear graphic of the three stages with arrows between to show progression:
1. We experience the stressor
2. Our brain interprets the stressor: Is it a threat? Is it friendly?
3. Our brain creates the appropriate stress response: physical, mental, emotional

And another graphic with illustrations of this process:
A charging lion
A brain thinking/interpreting the potential stressor
A person running away (the response to the threat).

Needs to be used for online learning course about stress and resilience.

See attached for assistance.

```html
<!DOCTYPE html>
<html lang="en">
<head>
<meta charset="utf-8">
<title>Stress Response Model</title>
<link rel="stylesheet" href="https://fonts.googleapis.com/css2?family=Montserrat:wght@400;500&display=swap">
<style>
  :root {
    --bg: #f0efeb;
    --card: #ffffff;
    --orange: #f5891b;
    --orange-dark: #e07812;
    --stone: #b4aaa0;
    --stone-dark: #9a918a;
    --gold: #eeb727;
    --gold-dark: #d9a000;
    --ink-light: #ffffff;
  }
  * { box-sizing: border-box; margin: 0; padding: 0; }
  html, body { width: 1200px; height: 771px; overflow: hidden; background: var(--bg); }
  .canvas { position: relative; width: 1200px; height: 771px; background: var(--bg); font-family: "Montserrat", sans-serif; }

  .stage-card {
    position: absolute; top: 153px; width: 288px; height: 464px;
    background: var(--card); border: 4px solid; border-radius: 20px;
  }
  .stage-card--experience { left: 52px; border-color: var(--orange); }
  .stage-card--interpret { left: 451px; border-color: var(--stone); }
  .stage-card--respond { left: 850px; border-color: var(--gold); }

  .stage-illustration {
    position: absolute; left: 30px; top: 30px; width: 220px; height: 260px; border-radius: 16px;
  }
  .stage-card--experience .stage-illustration { background: linear-gradient(160deg, #5c2c05 0%, #f4a54a 70%, #efe9e4 100%); }
  .stage-card--interpret .stage-illustration { background: linear-gradient(170deg, #fbe3d6 0%, #e55c63 35%, #f0be6e 70%, #efe9e4 100%); }
  .stage-card--respond .stage-illustration { background: linear-gradient(170deg, #f9b47c 0%, #e88b26 40%, #84451d 80%, #efe9e4 100%); }

  .stage-label {
    position: absolute; top: 468px; width: 339px; height: 74px;
    border-radius: 0 37px 37px 0;
    display: flex; align-items: center; justify-content: center; text-align: center;
    color: var(--ink-light); font-size: 16.5px; font-weight: 400; line-height: 1.22; letter-spacing: 0.2px;
    padding: 0 16px;
  }
  .stage-label--experience { left: 31px; background: var(--orange); }
  .stage-label--interpret { left: 430px; background: var(--stone); }
  .stage-label--respond { left: 829px; background: var(--gold); }

  .label-fold {
    position: absolute; top: 542px; width: 21px; height: 23px;
    clip-path: polygon(0 0, 100% 0, 100% 100%);
  }
  .label-fold--experience { left: 31px; background: var(--orange-dark); }
  .label-fold--interpret { left: 430px; background: var(--stone-dark); }
  .label-fold--respond { left: 829px; background: var(--gold-dark); }

  .flow-arrow { position: absolute; top: 348px; width: 67px; height: 79px; }
  .flow-arrow--first { left: 361px; }
  .flow-arrow--second { left: 760px; }
</style>
</head>
<body>
<main class="canvas">
  <section class="stage-card stage-card--experience">
    <div class="stage-illustration" role="img" aria-label="Illustration of a roaring lion charging forward"></div>
  </section>
  <div class="label-fold label-fold--experience"></div>
  <div class="stage-label stage-label--experience">We experience the stressor</div>

  <svg class="flow-arrow flow-arrow--first" viewBox="0 0 67 79" aria-hidden="true">
    <polygon points="0,20 20,20 20,0 67,39.5 20,79 20,59 0,59" fill="var(--orange)"/>
  </svg>

  <section class="stage-card stage-card--interpret">
    <div class="stage-illustration" role="img" aria-label="Illustration of a head with an exposed brain, question marks and a light bulb"></div>
  </section>
  <div class="label-fold label-fold--interpret"></div>
  <div class="stage-label stage-label--interpret">Our brain interprets the stressor:<br>Is it a threat? Is it friendly?</div>

  <svg class="flow-arrow flow-arrow--second" viewBox="0 0 67 79" aria-hidden="true">
    <polygon points="0,20 20,20 20,0 67,39.5 20,79 20,59 0,59" fill="var(--stone)"/>
  </svg>

  <section class="stage-card stage-card--respond">
    <div class="stage-illustration" role="img" aria-label="Illustration of a frightened person running away"></div>
  </section>
  <div class="label-fold label-fold--respond"></div>
  <div class="stage-label stage-label--respond">Our brain creates<br>the appropriate stress response:<br>physical, mental, emotional</div>
</main>
</body>
</html>
```